Real Estate Seller Financing Postcard

I need a postcard that lays out these options contained in the notes that grabs attention, explains the two options easily and is eye-catching. The front needs to have the percentages on it and information about it and on the other side One side exact Text is:
"Monthly income without tenant headaches" in big letters. Also on front "Get
110%
add an "or"
160% of market value for your property. ". The percentages should be displayed and that is not to be a sentence of text. Other side text: I need bullets points for these "Formal protection as a lien holder against home
No commission or closing cost
Fast closings possible
Property taken as is so no repairs.

Add to the top of the back in "It’s simple. I am a new investor without down payment capital who still want to double our portfolio this year to grow our portfolio."
Here are the two options that are to be the largest part of the back
Option 1, you can receive 80% now cash and 30% over a short period of time including interest.

Option 2, where act like a bank allowing you to make 150% if you finance the whole property(ies). No gimmicks and surprises, just simple unconventional financing.

Include Logo Somewhere

Target Market(s)

Property Owners Wanting to Sell Their Property

Industry/Entity Type

Real Estate Investing

Requirements
Must have
• The options promiment and each side with its respective information. Must have logo somewhere
Nice to have
• The options in color other than black.
Should not have
• A picture of money on the front. Any other image is okay.

```html
<!DOCTYPE html>
<html lang="en">
<head>
<meta charset="utf-8">
<title>Harbor Real Estate Group – Seller Financing Postcard</title>
<link href="https://fonts.googleapis.com/css2?family=Poppins:wght@300;400;500;600;700;800&family=Oswald:wght@600;700&display=swap" rel="stylesheet">
<style>
:root{
  --blue:#0b3a94;
  --blue-deep:#082c74;
  --blue-accent:#2456d6;
  --gray:#8b8b8b;
  --gray-light:#d9d9d9;
  --dark:#1f1f1f;
  --white:#ffffff;
  --page:#efefef;
  --ink:#1b1b1b;
}
*{box-sizing:border-box;margin:0;padding:0}
html,body{width:783px;height:1200px;overflow:hidden}
body{background:var(--page);font-family:"Poppins",sans-serif;position:relative}
.card{position:absolute;left:31px;width:720px;height:480px;background:var(--white);box-shadow:0 3px 10px rgba(0,0,0,.22);overflow:hidden}
.front{top:90px}
.back{top:630px}
.abs{position:absolute}

/* front */
.front-band{left:0;top:0;width:720px;height:288px;background:linear-gradient(180deg,#0e3c98 0%,var(--blue) 100%)}
.brand{display:flex;align-items:center;gap:10px;color:var(--white)}
.brand-dot{width:52px;height:52px;border:2px solid currentColor;border-radius:50%}
.brand-name{font-weight:500;line-height:1}
.brand-name .big{display:block;font-size:27px;letter-spacing:.5px}
.brand-name .small{display:block;font-size:9.5px;margin-top:3px}
.front .brand{left:32px;top:28px}
.headline{left:33px;top:86px;color:var(--white);font-weight:800;line-height:.95;text-transform:uppercase}
.headline .l1{display:block;font-size:56px;letter-spacing:-.5px}
.headline .l2{display:block;font-size:68px;letter-spacing:-1px}
.headline .sub{display:block;font-size:18.5px;font-weight:700;margin-top:6px;letter-spacing:.1px}
.badge{top:237px;width:92px;height:92px;border-radius:50%;background:var(--gray);border:3px solid var(--white);box-shadow:0 4px 6px rgba(0,0,0,.25);color:var(--white);text-align:center;padding-top:14px}
.badge .get{display:block;font-size:21px;font-weight:300;line-height:1}
.badge .pct{display:block;font-size:27px;font-weight:700;line-height:1.05}
.badge .rule{display:block;width:26px;height:2px;background:var(--white);margin:4px auto 0}
.photo-front{left:0;top:0}
.market-label{left:335px;top:298px;width:360px;height:30px;background:var(--gray);color:var(--white);font-size:16.5px;font-weight:500;text-align:center;line-height:30px;letter-spacing:.2px}
.perks{left:34px;top:350px;display:flex;gap:0;list-style:none}
.perks li{display:flex;gap:7px;font-size:13.5px;font-weight:600;line-height:1.2;color:var(--ink)}
.tick{flex:none;width:13px;height:13px;margin-top:2px}
.contact-bar{left:0;top:408px;width:720px;height:72px;background:var(--dark);display:flex;align-items:center;padding-left:36px;color:var(--white);font-weight:600}
.contact-bar .item{display:flex;align-items:center;gap:8px}
.contact-bar .phone{font-size:21px;font-weight:700;margin-right:22px}
.contact-bar .mail,.contact-bar .web{font-size:13.5px;margin-right:22px}
.icon{flex:none}

/* back */
.intro{left:36px;top:30px;width:250px;color:var(--white);font-size:11.5px;line-height:1.25;font-weight:400}
.intro b{font-weight:700}
.pill{background:var(--gray-light);color:var(--dark);font-size:11px;font-weight:700;padding:1px 7px;border-radius:0 8px 8px 0;letter-spacing:.3px}
.option-row{color:var(--white)}
.receive{left:37px;top:128px;font-size:12.5px;font-weight:400;color:var(--white)}
.big-num{font-family:"Oswald",sans-serif;font-weight:700;color:var(--white);line-height:1}
.num-80{left:36px;top:141px;font-size:44px}
.divider{background:rgba(255,255,255,.8);width:1px}
.opt1-text{left:136px;top:145px;color:var(--white);font-size:11.5px;line-height:1.2}
.opt1-text b{font-size:13px;font-weight:700;display:block}
.opt2-lead{left:37px;top:236px;width:92px;color:var(--white);font-size:11px;line-height:1.2}
.num-150{left:146px;top:232px;font-size:32px}
.finance{left:146px;top:269px;font-size:7.5px;font-weight:700;color:var(--white)}
.opt2-text{left:226px;top:236px;width:130px;color:var(--white);font-size:8px;line-height:1.25}
.thumb{top:300px;width:99px;height:74px;border:2px solid var(--white);border-radius:8px}
.back-bar{left:0;top:394px;width:395px;height:86px;background:var(--dark);padding:20px 0 0 36px;color:var(--white)}
.call{font-size:20px;font-weight:700;letter-spacing:.2px}
.call span{color:var(--blue-accent)}
.back-bar .row{display:flex;gap:10px;margin-top:4px;font-size:10px;font-weight:600}
.back-bar .row span{display:flex;align-items:center;gap:5px}
.back .brand{left:414px;top:34px;color:var(--blue)}
.back .brand-dot{width:46px;height:46px}
.back .brand-name .big{font-size:22px}
.back .brand-name .small{font-size:8px}
.stamp{left:626px;top:29px;width:62px;height:57px;background:var(--gray-light)}
.address-line{left:421px;width:268px;height:1px;background:#9a9a9a}
</style>
</head>
<body>

<!-- FRONT -->
<section class="card front" aria-label="Postcard front">
  <div class="abs front-band"></div>

  <svg class="abs photo-front" width="720" height="288" viewBox="0 0 720 288">
    <defs>
      <linearGradient id="photoTone" x1="0" y1="0" x2="0" y2="1">
        <stop offset="0" stop-color="#7f93b8"/>
        <stop offset=".45" stop-color="#b9c3d3"/>
        <stop offset="1" stop-color="#eef0f3"/>
      </linearGradient>
    </defs>
    <path d="M368 175 A150 150 0 0 1 666 175" fill="none" stroke="#ffffff" stroke-width="2"/>
    <polygon points="338,288 338,168 410,135 410,82 520,40 626,82 626,135 694,168 694,288" fill="#8a8a8a"/>
    <polygon role="img" aria-label="Photo of a small model house on a table between stacks of coins" points="344,288 344,172 416,139 416,86 520,46 620,86 620,139 688,172 688,288" fill="url(#photoTone)"/>
  </svg>

  <div class="abs brand">
    <span class="brand-dot"></span>
    <span class="brand-name"><span class="big">HARBOR</span><span class="small">REAL ESTATE GROUP</span></span>
  </div>

  <h1 class="abs headline">
    <span class="l1">Monthly</span>
    <span class="l2">Income</span>
    <span class="sub">Without Tenant Headaches</span>
  </h1>

  <div class="abs badge" style="left:33px"><span class="get">GET</span><span class="pct">100%</span><span class="rule"></span></div>
  <div class="abs badge" style="left:135px"><span class="get">GET</span><span class="pct">110%</span><span class="rule"></span></div>
  <div class="abs badge" style="left:235px"><span class="get">GET</span><span class="pct">160%</span><span class="rule"></span></div>

  <div class="abs market-label">OF MARKET VALUE FOR YOUR PROPERTY</div>

  <ul class="abs perks">
    <li style="width:212px"><svg class="tick" viewBox="0 0 14 14"><circle cx="7" cy="7" r="7" fill="#0b3a94"/><path d="M3.8 7.2l2.2 2.1 4.2-4.4" fill="none" stroke="#fff" stroke-width="1.6"/></svg><span>Formal protection as a<br>lien holder against home</span></li>
    <li style="width:148px"><svg class="tick" viewBox="0 0 14 14"><circle cx="7" cy="7" r="7" fill="#0b3a94"/><path d="M3.8 7.2l2.2 2.1 4.2-4.4" fill="none" stroke="#fff" stroke-width="1.6"/></svg><span>No commission<br>or closing cost</span></li>
    <li style="width:130px"><svg class="tick" viewBox="0 0 14 14"><circle cx="7" cy="7" r="7" fill="#0b3a94"/><path d="M3.8 7.2l2.2 2.1 4.2-4.4" fill="none" stroke="#fff" stroke-width="1.6"/></svg><span>Fast closings<br>possible</span></li>
    <li style="width:170px"><svg class="tick" viewBox="0 0 14 14"><circle cx="7" cy="7" r="7" fill="#0b3a94"/><path d="M3.8 7.2l2.2 2.1 4.2-4.4" fill="none" stroke="#fff" stroke-width="1.6"/></svg><span>Property taken as<br>is so no repairs</span></li>
  </ul>

  <div class="abs contact-bar">
    <span class="item phone"><svg class="icon" width="20" height="20" viewBox="0 0 24 24"><path d="M6.6 10.8a15 15 0 006.6 6.6l2.2-2.2c.3-.3.7-.4 1-.2 1.1.4 2.3.6 3.6.6.6 0 1 .4 1 1V20c0 .6-.4 1-1 1A17 17 0 013 4c0-.6.4-1 1-1h3.5c.6 0 1 .4 1 1 0 1.3.2 2.5.6 3.6.1.3 0 .7-.2 1z" fill="#2456d6"/></svg>012.555.0147</span>
    <span class="item mail"><svg class="icon" width="20" height="14" viewBox="0 0 20 14"><rect width="20" height="14" fill="#2456d6"/><path d="M0 0l10 7 10-7" fill="none" stroke="#fff" stroke-width="1.4"/></svg>harborestates@example.com</span>
    <span class="item web"><svg class="icon" width="18" height="18" viewBox="0 0 20 20"><g fill="none" stroke="#2456d6" stroke-width="1.6"><circle cx="10" cy="10" r="8.5"/><ellipse cx="10" cy="10" rx="4" ry="8.5"/><path d="M1.5 10h17M3 5.5h14M3 14.5h14"/></g></svg>www.harborestates.example</span>
  </div>
</section>

<!-- BACK -->
<section class="card back" aria-label="Postcard back">
  <svg class="abs" style="left:0;top:0" width="400" height="394" viewBox="0 0 400 394">
    <polygon points="0,0 258,0 338,62 338,165 400,195 400,394 0,394" fill="#9a9a9a"/>
    <polygon points="0,0 250,0 332,64 332,168 394,198 394,394 0,394" fill="#0b3a94"/>
    <rect x="0" y="108" width="332" height="86" fill="#082c74" opacity=".55"/>
    <rect x="0" y="206" width="394" height="78" fill="#082c74" opacity=".55"/>
  </svg>

  <p class="abs intro"><b>It’s simple.</b> I am a new investor without down payment capital who still want to double our portfolio this year to grow our portfolio.</p>

  <span class="abs pill" style="left:36px;top:97px">OPTION 1</span>
  <span class="abs receive">YOU CAN RECEIVE</span>
  <span class="abs big-num num-80">80%</span>
  <span class="abs divider" style="left:128px;top:146px;height:40px"></span>
  <p class="abs opt1-text"><b>NOW CASH</b>and 30% over a short period<br>of time including interest.</p>

  <span class="abs pill" style="left:36px;top:206px">OPTION 2</span>
  <p class="abs opt2-lead">Where act like a bank allowing you to make</p>
  <span class="abs divider" style="left:136px;top:236px;height:40px"></span>
  <span class="abs big-num num-150">150%</span>
  <span class="abs finance">IF YOU FINANCE</span>
  <p class="abs opt2-text">The whole property(ies). No gimmicks and surprises, just simple unconventional financing.</p>

  <div class="abs thumb" role="img" aria-label="Photo of paperwork being signed at a desk" style="left:36px;background:linear-gradient(135deg,#e9e4dc,#a89580)"></div>
  <div class="abs thumb" role="img" aria-label="Photo of a couple reviewing documents with an agent" style="left:152px;background:linear-gradient(135deg,#6f8fa6,#c47a4d)"></div>
  <div class="abs thumb" role="img" aria-label="Photo of a suburban street with houses" style="left:268px;background:linear-gradient(180deg,#8fb6e6 0%,#d8cfc2 55%,#58605f 100%)"></div>

  <div class="abs back-bar">
    <div class="call"><span>CALL US NOW:</span> 012.555.0147</div>
    <div class="row">
      <span><svg width="13" height="9" viewBox="0 0 20 14"><rect width="20" height="14" fill="#2456d6"/><path d="M0 0l10 7 10-7" fill="none" stroke="#fff" stroke-width="1.4"/></svg>harborestates@example.com</span>
      <span><svg width="12" height="12" viewBox="0 0 20 20"><g fill="none" stroke="#2456d6" stroke-width="1.8"><circle cx="10" cy="10" r="8.5"/><ellipse cx="10" cy="10" rx="4" ry="8.5"/><path d="M1.5 10h17"/></g></svg>www.harborestates.example</span>
    </div>
  </div>

  <div class="abs brand">
    <span class="brand-dot"></span>
    <span class="brand-name"><span class="big">HARBOR</span><span class="small">REAL ESTATE GROUP</span></span>
  </div>
  <div class="abs stamp"></div>
  <div class="abs address-line" style="top:190px"></div>
  <div class="abs address-line" style="top:233px"></div>
  <div class="abs address-line" style="top:272px"></div>
  <div class="abs address-line" style="top:316px"></div>
</section>

</body>
</html>
```